Business Card Design

Our Pharmacy Opens late - the last to close in Brisbane
over 30 years since opened.
Open from 7am - 11pm every day.
Next to Corbrook 7 Day Medical Centre
Parking in front of shop
Sit with a pharmacist for every script - the best advice every time.
Private consulting room.
We have the medication that you need.
Wide range Home Health Care products.

Looking for a card that my (young) staff feel happy to hand out to people they they meet.
Updates

Hello Many thanks for your submissions I just need to clarify the costings for this project as per my updated brief Please confirm then we can proceed Many thanks Desmond

Reason: due to the adjusted brief and query I have extended the deadline Many thanks for those that have submitted, I will choose the designer as soon as I understand the costings of the project, as per the message despatched today Regards desmond

Target Market(s)

men and women 30-70

Industry/Entity Type

Business

Contact Information for Business Card

Pelworth Pharmacy - Corbrook
317 Tolland Rd
Corbrook 4186
Last to Close
Open 7am - 11pm

Font styles to use
Sans Serif

Requirements
Must have
• each batch of 250 will have the following staff names

Lorraine Muskett, Senior Pharmacist
Fatima Oduya, Pharmacist
Bo Lam, Pharmacist
Ondine Whitlaw, Pharmacist
Greta Volm, Retail Manager
Tess Ruvolo, Marketing Manager
Desmond Pelworth, Pharmacist Proprietor
Should not have
• Please advise if the cost of this job covers the 7 individualised business cards.

Each staff member needs their own card.

please advise

```html
<!DOCTYPE html>
<html lang="en">
<head>
<meta charset="utf-8">
<title>Pelworth Pharmacy – Business Card</title>
<link rel="stylesheet" href="https://fonts.googleapis.com/css2?family=Arimo:ital,wght@0,400;0,700;1,700&display=swap">
<style>
  :root {
    --navy: #2b3286;
    --yellow: #f7e400;
    --white: #ffffff;
    --ink: #111111;
    --backdrop: #e9eaee;
  }
  * { margin: 0; padding: 0; box-sizing: border-box; }
  html, body {
    width: 1200px;
    height: 523px;
    overflow: hidden;
    background: var(--backdrop);
    font-family: "Arimo", Arial, sans-serif;
  }
  .canvas {
    position: relative;
    width: 1200px;
    height: 523px;
    display: flex;
    align-items: center;
    justify-content: center;
  }
  .business-card {
    position: relative;
    width: 840px;
    height: 480px;
    background: var(--white);
    overflow: hidden;
    box-shadow: 0 6px 24px rgba(0, 0, 0, 0.18);
  }
  .card-bands {
    position: absolute;
    inset: 0;
    width: 840px;
    height: 480px;
  }
  .staff-name {
    position: absolute;
    left: 30px;
    top: 42px;
    color: var(--yellow);
    font-weight: 700;
    font-size: 42px;
    letter-spacing: 0.3px;
    text-transform: uppercase;
    white-space: nowrap;
  }
  .staff-role {
    position: absolute;
    left: 592px;
    top: 56px;
    color: var(--ink);
    font-weight: 700;
    font-style: italic;
    font-size: 24px;
    white-space: nowrap;
  }
  .brand {
    position: absolute;
    left: 40px;
    top: 240px;
    display: flex;
    align-items: center;
    gap: 14px;
  }
  .brand-dot {
    width: 40px;
    height: 40px;
    border-radius: 50%;
    background: var(--yellow);
    flex: none;
  }
  .brand-name {
    color: var(--navy);
    font-weight: 700;
    font-size: 32px;
    white-space: nowrap;
  }
  .store-details {
    position: absolute;
    left: 445px;
    top: 190px;
    color: var(--ink);
    font-weight: 700;
    font-size: 27px;
    line-height: 36px;
  }
  .store-address {
    margin-top: 16px;
    font-size: 25px;
    line-height: 34px;
  }
</style>
</head>
<body>
  <main class="canvas">
    <article class="business-card">
      <svg class="card-bands" viewBox="0 0 840 480" aria-hidden="true">
        <path fill="var(--navy)" d="M0 0 H840 V42 H630 C590 42 570 60 550 90 C532 116 510 128 470 128 H0 Z"/>
        <path fill="var(--yellow)" d="M630 42 H840 V98 H544 C560 74 580 42 630 42 Z"/>
        <rect fill="var(--yellow)" x="0" y="404" width="840" height="12"/>
        <rect fill="var(--navy)" x="0" y="416" width="840" height="64"/>
      </svg>

      <h1 class="staff-name">Lorraine Muskett</h1>
      <p class="staff-role">Senior Pharmacist</p>

      <div class="brand">
        <span class="brand-dot"></span>
        <span class="brand-name">Pelworth Pharmacy</span>
      </div>

      <div class="store-details">
        <p class="store-hours">OPEN: 7am - 11pm</p>
        <p class="store-phone">Phone: 555-0142</p>
        <p class="store-email">Email:</p>
        <p class="store-address">Corbrook 317 Tolland<br>Rd Corbrook 4186</p>
      </div>
    </article>
  </main>
</body>
</html>
```